Hacienda Vista Moreno Business cards

We would like 3 individual business cards with the logo you designed:

1) Dana Perlwitz - Phone: 206 417 6093
2) Theodore M Perlwitz - Phone 206 581 2746
3) Marta Bylund - Phone 310-864-2071

Address for all three cards:
7128 284th Ave NE
Carnation, WA 98019
HaciendaVistaMoreno@mailbrook.net

Industry/Entity Type

Business

```html
<!DOCTYPE html>
<html lang="en">
<head>
<meta charset="utf-8">
<title>Hacienda Vista Moreno — Business Card</title>
<link rel="stylesheet" href="https://fonts.googleapis.com/css2?family=Cinzel:wght@400&family=Open+Sans:wght@400&display=swap">
<style>
  :root {
    --page-bg: #ebe8e5;
    --card-bg: #ffffff;
    --scene-dark: #d6d6d6;
    --scene-light: #ececec;
    --ink: #141414;
    --ink-soft: #6a6a6a;
    --card-shadow: rgba(0, 0, 0, 0.12);
  }
  * { box-sizing: border-box; margin: 0; padding: 0; }
  html, body {
    width: 1200px;
    height: 997px;
    overflow: hidden;
    background: var(--page-bg);
  }
  .stage {
    position: relative;
    width: 1200px;
    height: 997px;
  }
  .business-card {
    position: absolute;
    left: 180px;
    top: 258px;
    width: 840px;
    height: 480px;
    background: var(--card-bg);
    box-shadow: 0 10px 30px var(--card-shadow);
    overflow: hidden;
  }
  .card-scene {
    position: absolute;
    left: 0;
    top: 0;
    width: 100%;
    height: 62%;
    background:
      linear-gradient(180deg, rgba(255,255,255,0) 55%, var(--card-bg) 100%),
      linear-gradient(90deg, var(--scene-light) 0%, var(--scene-dark) 45%, var(--scene-light) 100%);
  }
  .card-content {
    position: absolute;
    left: 70px;
    top: 170px;
    right: 60px;
  }
  .brand-name {
    font-family: "Cinzel", serif;
    font-weight: 400;
    font-size: 40px;
    letter-spacing: 1px;
    color: var(--ink);
    line-height: 1.1;
  }
  .holder-name {
    margin-top: 42px;
    margin-left: 60px;
    font-family: "Cinzel", serif;
    font-size: 20px;
    letter-spacing: 1.5px;
    color: var(--ink-soft);
  }
  .contact-lines {
    margin-top: 44px;
    font-family: "Open Sans", sans-serif;
    font-size: 19px;
    line-height: 1.5;
    color: var(--ink);
  }
  .contact-lines .phone { margin-right: 18px; }
  .contact-lines .address { display: block; margin-left: 26px; }
</style>
</head>
<body>
  <main class="stage">
    <article class="business-card">
      <div class="card-scene" role="img" aria-label="Faded grey ranch scene with a wooden fence and a grazing horse"></div>
      <div class="card-content">
        <h1 class="brand-name">Hacienda Vista Moreno</h1>
        <p class="holder-name">Dana Perlwitz</p>
        <p class="contact-lines">
          <span class="phone">P: 206 417 6093</span><span class="email">HaciendaVistaMoreno@mailbrook.net</span>
          <span class="address">7128 284th Ave NE Carnation, WA 98019</span>
        </p>
      </div>
    </article>
  </main>
</body>
</html>
```